Harlow Capital - Financial Planning Solutions

Harlow Capital is a financial planning business in Melbourne, Australia. We cater to all kinds of clients from high net worth individuals to young people just starting a career. We need a chart, which will be included in client pitches, presentations and on our website, that conveys the various areas that we are able to provide client solutions.
We have attached three rudimentary interpretations of what we're talking about, one of which includes our logo. With each area of advice we have included a brief description of what it is. The different areas are not necessarily linked, so it's not a circular process but there is a logical progression to them: clients can ask us to get involved with any of the steps.
We are pretty open to suggestions as to the best presentation but are quite interested in an infographics approach.
You can check out our website at www.harlowcapital.com.au to see a bit about us, but please be aware that we are changing our investment philosophy and the tone of the website to a broader appeal.
Cheers, Oliver

Industry/Entity Type

Investment

```html
<!DOCTYPE html>
<html lang="en">
<head>
<meta charset="utf-8">
<title>Harlow Capital – Client Solutions</title>
<link rel="stylesheet" href="https://fonts.googleapis.com/css2?family=Montserrat:wght@300;400&family=Open+Sans:wght@400&family=Tinos&display=swap">
<style>
  :root {
    --paper: #e6e7e9;
    --ink: #000000;
    --gold: #a39a74;
    --white: #ffffff;
    --title: #111111;
  }
  * { margin: 0; padding: 0; box-sizing: border-box; }
  html, body {
    width: 1200px; height: 927px; overflow: hidden;
    background: var(--paper);
  }
  .sheet {
    position: relative;
    width: 1200px; height: 927px;
    background: var(--paper);
  }
  .sheet-title {
    position: absolute; left: 30px; top: 58px;
    font-family: "Montserrat", sans-serif; font-weight: 300;
    font-size: 47px; letter-spacing: 0.07em;
    color: var(--title); line-height: 1;
  }
  .brand {
    position: absolute; right: 26px; top: 56px;
    display: flex; align-items: center; gap: 14px;
  }
  .brand-mark {
    width: 30px; height: 30px; background: var(--ink);
  }
  .brand-name {
    font-family: "Montserrat", sans-serif; font-weight: 400;
    font-size: 27px; letter-spacing: 0.12em; color: var(--ink);
    line-height: 1;
  }
  .solution {
    position: absolute;
    left: var(--x); top: var(--top);
    width: 121px; height: calc(873px - var(--top));
  }
  .solution-label {
    height: var(--cap);
    background: var(--gold);
    color: var(--white);
    font-family: "Open Sans", sans-serif; font-size: 13.5px;
    line-height: 1.2; text-align: center; text-transform: uppercase;
    padding-top: var(--pad);
  }
  .solution-body {
    position: absolute; left: 0; right: 0;
    top: var(--cap); bottom: 0;
    background: var(--ink);
    clip-path: polygon(0 0, 100% 0, 100% 100%, 50% calc(100% - 73px), 0 100%);
  }
  .solution-text {
    position: absolute; left: 11px; right: 6px;
    top: calc(656px - var(--top) - var(--cap));
    font-family: "Tinos", serif; font-size: 14.5px; line-height: 21px;
    color: var(--white);
  }
</style>
</head>
<body>
<main class="sheet">
  <h1 class="sheet-title">CLIENT SOLUTIONS</h1>

  <div class="brand">
    <span class="brand-mark"></span>
    <span class="brand-name">HARLOW CAPITAL</span>
  </div>

  <section class="solution" style="--x:30px; --top:179px; --cap:106px; --pad:30px;">
    <h2 class="solution-label">Household<br>Income</h2>
    <div class="solution-body"><p class="solution-text">Funds<br>earned from<br>work or<br>investments</p></div>
  </section>

  <section class="solution" style="--x:179px; --top:229px; --cap:85px; --pad:28px;">
    <h2 class="solution-label">Tax Advice</h2>
    <div class="solution-body"><p class="solution-text">Maximise after<br>tax income</p></div>
  </section>

  <section class="solution" style="--x:326px; --top:288px; --cap:68px; --pad:19px;">
    <h2 class="solution-label">Financial<br>Planning</h2>
    <div class="solution-body"><p class="solution-text">A road map for<br>the application<br>of your after<br>tax income</p></div>
  </section>

  <section class="solution" style="--x:474px; --top:359px; --cap:61px; --pad:14px;">
    <h2 class="solution-label">Debt</h2>
    <div class="solution-body"><p class="solution-text">To fund the<br>purchase of a<br>house or<br>other asset</p></div>
  </section>

  <section class="solution" style="--x:621px; --top:359px; --cap:61px; --pad:11px;">
    <h2 class="solution-label">Super<br>Annuation</h2>
    <div class="solution-body"><p class="solution-text">Advice on<br>structuring and<br>management</p></div>
  </section>

  <section class="solution" style="--x:762px; --top:288px; --cap:68px; --pad:14px;">
    <h2 class="solution-label">Investment<br>Portfolio</h2>
    <div class="solution-body"><p class="solution-text">Optimise the<br>return on your<br>after tax<br>income</p></div>
  </section>

  <section class="solution" style="--x:911px; --top:229px; --cap:85px; --pad:28px;">
    <h2 class="solution-label" style="font-size:12.5px;">Insurance &amp;<br>Risk Protection</h2>
    <div class="solution-body"><p class="solution-text">Protect the<br>lifestyle<br>you’ve built<br>for you and<br>your family</p></div>
  </section>

  <section class="solution" style="--x:1058px; --top:179px; --cap:106px; --pad:30px;">
    <h2 class="solution-label">Estate<br>Planning</h2>
    <div class="solution-body"><p class="solution-text">Ensure your<br>assets are<br>dealt with as<br>you want</p></div>
  </section>
</main>
</body>
</html>
```